(draft #51)
please have the below adjustment in your design and they are:
- please change the slide color to become the same color as business card color background.
-#9 the folder inside is not shown kindly try to include if you can.
-please include an A4 Envelope, CD cover, Invoice & Flyer it is very important.
(draft #54)
-in the cd cover please include the address.
-the word oil changing service is needed below each logo.
-in the business card will you enlarge the name and push the address to the right little bit.
-please include an A4 Envelope, Invoice & Flyer it is very important.
(draft #56)
i would like to have some adjustment please and they are:
-in the letter head please will you spread the address horizontally and place it below or at the lower of the letterhead.
-in the Envelope will you take out the phone, fax, mobile and email from the upper side and place it in the lower side.
-in the folder with pocket there is no need for the mobile number and email
-please include an A4 Envelope & Flyer it is very important.
We need data for flyer.
kindly provide it.
please include all stationery like draft 59 and 60.
-please include an A4 Envelope, CD, & Flyer it is very important.
kindly delete the tilted designs logo only the horizontal drops.
but thanks again for your quick action.
thanks again
1- Please include a Folder with 1 or 2 pockets
2- master & theme slides for power point if possible.
i have uploaded the Al and eps files as per your requests and i am hoping to see good designs from you.

```html
<!DOCTYPE html>
<html lang="en">
<head>
<meta charset="utf-8">
<title>Torqline Stationery and Slides</title>
<link href="https://fonts.googleapis.com/css2?family=Montserrat:wght@400;600;700;800&display=swap" rel="stylesheet">
<style>
:root{
  --bg:#e9e6e1;
  --orange:#d9501f;
  --orange-deep:#a8320f;
  --orange-light:#ef6a2c;
  --gold:#d6a247;
  --paper:#ffffff;
  --ink:#3a3a3a;
  --muted:#8a8a8a;
  --faint:#f3e4dc;
}
*{margin:0;padding:0;box-sizing:border-box}
html,body{width:1200px;height:734px;overflow:hidden;background:var(--bg);font-family:'Montserrat',sans-serif}
.canvas{position:relative;width:1200px;height:734px}
.sheet{position:absolute;overflow:hidden;box-shadow:0 4px 10px rgba(0,0,0,.25)}
.cover-orange{background:radial-gradient(ellipse at 40% 45%,var(--orange-light),var(--orange) 45%,var(--orange-deep))}
.paper{background:var(--paper)}
.brand{position:absolute;display:flex;align-items:center;gap:7px;font-weight:800;letter-spacing:-.3px}
.brand .dot{border-radius:50%}
.brand.on-orange{color:#fff}
.brand.on-orange .dot{background:#fff}
.brand.on-paper{color:var(--orange)}
.brand.on-paper .dot{background:var(--orange)}
.faint-mark{position:absolute;border-radius:50%;background:var(--faint);opacity:.8}
.contact{position:absolute;color:#fff;font-size:6px;line-height:9px;opacity:.9}
.contact p.gap{margin-top:6px}
.swoosh{position:absolute;left:0;bottom:0;width:100%}
.slide-title{position:absolute;color:var(--orange);font-weight:700;font-size:17px}
.slide-sub{position:absolute;color:var(--ink);font-size:11px;font-weight:600}
.about h2{position:absolute;left:14px;top:14px;color:var(--orange-deep);font-size:17px;font-weight:800}
.about .body{position:absolute;left:14px;top:54px;width:168px;color:var(--ink);font-size:6.5px;line-height:9px}
.about h3{font-size:8px;font-weight:700;margin:6px 0 3px}
.about .sidebar{position:absolute;right:0;top:0;width:44px;height:100%;background:linear-gradient(var(--orange),var(--orange-deep))}
.thanks{position:absolute;left:0;width:100%;text-align:center;color:#fff}
</style>
</head>
<body>
<div class="canvas">

  <!-- Open folder: outer cover -->
  <section class="sheet cover-orange" style="left:67px;top:79px;width:245px;height:401px">
    <div class="brand on-orange" style="left:30px;top:178px;font-size:21px"><span class="dot" style="width:14px;height:14px"></span>Torqline</div>
    <div class="contact" style="left:145px;top:270px">
      <p>PO Box 4410</p><p>Harbour Road, Doha</p>
      <p class="gap">T +974 4400 1200</p><p>F +974 4400 1201</p>
    </div>
    <svg class="swoosh" viewBox="0 0 245 60" height="60" preserveAspectRatio="none">
      <path d="M0 42 Q120 20 245 0 L245 60 L0 60Z" fill="var(--gold)"/>
      <path d="M0 50 Q120 30 245 10 L245 60 L0 60Z" fill="var(--orange-deep)"/>
    </svg>
  </section>
  <section class="sheet paper" style="left:312px;top:79px;width:259px;height:401px">
    <div class="brand on-paper" style="left:14px;top:16px;font-size:16px"><span class="dot" style="width:11px;height:11px"></span>Torqline</div>
    <div class="faint-mark" style="left:70px;top:90px;width:170px;height:170px"></div>
    <svg class="swoosh" viewBox="0 0 259 90" height="90" preserveAspectRatio="none">
      <path d="M0 90 Q150 50 259 0 L259 90Z" fill="var(--gold)"/>
      <path d="M0 90 Q160 62 259 22 L259 90Z" fill="var(--orange)"/>
    </svg>
  </section>

  <!-- Folder inside with pocket -->
  <section class="sheet paper" style="left:595px;top:79px;width:264px;height:401px">
    <div class="brand on-paper" style="left:14px;top:16px;font-size:16px"><span class="dot" style="width:11px;height:11px"></span>Torqline</div>
    <div class="faint-mark" style="left:70px;top:90px;width:170px;height:170px"></div>
    <svg style="position:absolute;left:0;top:290px" width="264" height="111" viewBox="0 0 264 111" preserveAspectRatio="none">
      <path d="M0 20 Q130 34 264 0 L264 111 L0 111Z" fill="#f7f7f7" stroke="#dddddd"/>
    </svg>
  </section>

  <!-- Folder front cover -->
  <section class="sheet cover-orange" style="left:893px;top:79px;width:254px;height:401px">
    <div class="brand on-orange" style="left:40px;top:178px;font-size:21px"><span class="dot" style="width:14px;height:14px"></span>Torqline</div>
    <div class="contact" style="left:150px;top:270px">
      <p>PO Box 4410</p><p>Harbour Road, Doha</p>
      <p class="gap">T +974 4400 1200</p><p>F +974 4400 1201</p>
    </div>
    <svg class="swoosh" viewBox="0 0 254 60" height="60" preserveAspectRatio="none">
      <path d="M0 52 Q130 36 254 12 L254 60 L0 60Z" fill="var(--gold)"/>
      <path d="M0 58 Q130 44 254 22 L254 60 L0 60Z" fill="var(--orange-deep)"/>
    </svg>
  </section>

  <!-- Title slide -->
  <section class="sheet paper" style="left:240px;top:504px;width:252px;height:216px">
    <div class="brand on-paper" style="left:12px;top:12px;font-size:15px"><span class="dot" style="width:10px;height:10px"></span>Torqline</div>
    <div class="faint-mark" style="left:140px;top:40px;width:110px;height:110px"></div>
    <div class="slide-title" style="left:14px;top:120px">YOUR TITLE GOES HERE</div>
    <div class="slide-sub" style="left:14px;top:144px">Company Name</div>
    <svg class="swoosh" viewBox="0 0 252 50" height="50" preserveAspectRatio="none">
      <path d="M0 40 Q130 30 252 0 L252 50 L0 50Z" fill="var(--gold)"/>
      <path d="M0 46 Q130 38 252 10 L252 50 L0 50Z" fill="var(--orange)"/>
    </svg>
  </section>

  <!-- About slide -->
  <section class="sheet paper about" style="left:504px;top:504px;width:252px;height:216px">
    <div class="sidebar"></div>
    <h2>ABOUT US</h2>
    <div class="body">
      <h3>Content 1:</h3>
      <p>We keep engines running smoothly with fast oil changes, careful inspections and quality lubricants. Our trained team serves private drivers and business fleets every day of the week.</p>
      <h3>Content 2:</h3>
      <p>Book a visit online or drop by any branch. Most services are finished in under thirty minutes while you relax in our comfortable waiting lounge.</p>
    </div>
    <svg class="swoosh" viewBox="0 0 252 34" height="34" preserveAspectRatio="none">
      <path d="M0 30 Q130 24 252 0 L252 34 L0 34Z" fill="var(--gold)"/>
      <path d="M0 34 Q130 30 252 8 L252 34Z" fill="var(--orange)"/>
    </svg>
  </section>

  <!-- Thank-you slide -->
  <section class="sheet cover-orange" style="left:780px;top:504px;width:252px;height:216px">
    <div class="brand on-orange" style="left:68px;top:78px;font-size:23px"><span class="dot" style="width:15px;height:15px"></span>Torqline</div>
    <div class="thanks" style="top:150px;font-size:10.5px;font-weight:700">THANK YOU FOR YOUR ATTENTION</div>
    <div class="thanks" style="top:166px;font-size:7.5px;font-weight:600">PRESENTER</div>
  </section>

</div>
</body>
</html>
```